dsadasdasdasdsa

Industry/Entity Type

Mortgage Broking

Requirements
Must have
• Call-to-action button somewhere on the graphic
Nice to have
• The font of our logo is Montserrat

```html
<!DOCTYPE html>
<html lang="en">
<head>
<meta charset="utf-8">
<title>Mortgage Broker Directory Banner</title>
<link href="https://fonts.googleapis.com/css2?family=Montserrat:wght@500;600&display=swap" rel="stylesheet">
<style>
  :root {
    --backdrop: #3a3a3a;
    --green-deep: #15784a;
    --green-mid: #4e9e43;
    --green-lime: #8dc63f;
    --green-pale: #e6f2dc;
    --ring-dark: #178247;
    --ring-light: #3bab3c;
    --ring-lime: #8ccf3e;
    --ring-grey: #d2d2d4;
    --panel-white: #ffffff;
    --headline: #164c31;
    --cta-bg: #6e1d13;
    --cta-text: #ffffff;
  }
  * { box-sizing: border-box; margin: 0; padding: 0; }
  html, body { width: 1200px; height: 1200px; overflow: hidden; }
  body { background: var(--backdrop); position: relative; font-family: "Montserrat", sans-serif; }

  .banner {
    position: absolute; left: 47px; top: 550px; width: 1103px; height: 151px;
    overflow: hidden;
    background: linear-gradient(90deg, var(--green-deep) 0%, var(--green-mid) 20%, var(--green-lime) 32%, #c3e2a0 47%, var(--green-pale) 62%, #eef6e6 80%, #f4f9ef 100%);
    box-shadow: 0 0 26px rgba(0,0,0,0.55);
  }
  .scene-illustration {
    position: absolute; left: 16px; top: 6px; width: 204px; height: 141px;
    border-radius: 8px;
    background: linear-gradient(180deg, rgba(255,255,255,0.10), rgba(255,255,255,0.18));
  }
  .headline {
    position: absolute; left: 0; width: 1118px; top: 30px;
    text-align: center; font-weight: 600; font-size: 37px; line-height: 1;
    color: var(--headline); letter-spacing: 0.2px;
  }
  .cta {
    position: absolute; left: 323px; top: 85px; width: 470px; height: 29px;
    background: var(--cta-bg); color: var(--cta-text); border-radius: 5px;
    font-weight: 500; font-size: 20px; line-height: 29px; text-align: center;
    text-decoration: none; letter-spacing: 0.2px;
    box-shadow: 0 1px 2px rgba(0,0,0,0.25);
  }
  .corner-rings { position: absolute; left: 0; top: 0; }
  .mascot {
    position: absolute; left: 987px; top: 2px; width: 97px; height: 147px;
    border-radius: 40px 40px 20px 20px;
    background: linear-gradient(160deg, #4fae5a 0%, #2f8f49 45%, #a8643a 75%, #6f4425 100%);
  }
</style>
</head>
<body>
  <section class="banner">
    <div class="scene-illustration" role="img" aria-label="Outline drawing of a house between two trees with clouds above"></div>

    <h1 class="headline">Need a Mortgage Broker?</h1>
    <a class="cta" href="#">Search Now on Australia's Largest Directory</a>

    <svg class="corner-rings" width="1103" height="151" viewBox="0 0 1103 151" aria-hidden="true">
      <circle cx="1082" cy="10" r="191" fill="var(--ring-dark)"/>
      <circle cx="1082" cy="10" r="171" fill="var(--ring-light)"/>
      <circle cx="1082" cy="10" r="165" fill="var(--ring-lime)"/>
      <circle cx="1082" cy="10" r="161" fill="var(--panel-white)"/>
      <circle cx="1082" cy="10" r="155" fill="var(--ring-grey)"/>
      <circle cx="1082" cy="10" r="149" fill="var(--panel-white)"/>
    </svg>

    <div class="mascot" role="img" aria-label="Friendly cartoon turtle mascot pointing toward the headline"></div>
  </section>
</body>
</html>
```